Mesh Banner Design for Business Premises

We require the design of a large mesh banner to be installed across the front fence of our warehouse. The banner should prominently feature our existing Trelborn logo and brand colours (yellow, white, and black) and be designed to be highly visible from the road.

The overall aesthetic should be strong, masculine, and industrial, reflecting the nature of the scaffolding and construction industry. The background should be predominantly black, with our branding incorporated in yellow and white for strong contrast and readability.

The banner should clearly communicate the full scope of services we provide, including:

Scaffold Design
Scaffold Engineering
Scaffold Installation / Erection
Scaffold Dismantling

It should also indicate the types of projects and clients we service, including:

Commercial
Industrial
Residential
Civil

The design should feel bold and professional, with a construction-oriented style that aligns with the scaffolding industry. It should be clean, impactful, and easy to read from a distance, ensuring passing traffic can quickly understand our services.

Where possible, subtle industrial or structural design elements (such as scaffold components, steel textures, or linework) may be incorporated into the background to reinforce the industry theme while keeping the layout uncluttered.

The final design will be produced as a large-format mesh banner for outdoor installation, so it should be created with this application and viewing distance in mind.

```html
<!DOCTYPE html>
<html lang="en">
<head>
<meta charset="utf-8">
<title>Trelborn Mesh Banner</title>
<link rel="stylesheet" href="https://fonts.googleapis.com/css2?family=Saira+Semi+Condensed:wght@600;700&display=swap">
<style>
  :root {
    --page: #ffffff;
    --black: #111111;
    --steel-dark: #1a1a1a;
    --steel-mid: #3a3a3a;
    --steel-light: #5a5a5a;
    --yellow: #f2b01e;
    --white: #ffffff;
  }
  * { margin: 0; padding: 0; box-sizing: border-box; }
  html, body {
    width: 1200px; height: 1200px; overflow: hidden;
    background: var(--page);
  }
  .banner {
    position: absolute;
    left: 22px; top: 443px;
    width: 1157px; height: 208px;
    background: var(--black);
    overflow: hidden;
    font-family: "Saira Semi Condensed", sans-serif;
  }
  .banner__backdrop {
    position: absolute; inset: 0;
    background:
      radial-gradient(ellipse at 45% 35%, var(--steel-light) 0%, var(--steel-mid) 35%, var(--steel-dark) 75%),
      var(--black);
  }
  .banner__graphics {
    position: absolute; inset: 0;
    width: 100%; height: 100%;
  }
  .brand-name {
    position: absolute;
    left: 55px; top: 146px;
    width: 290px;
    text-align: center;
    color: var(--white);
    font-weight: 600;
    font-size: 26px;
    letter-spacing: 0.42em;
    text-indent: 0.42em;
    line-height: 1;
  }
  .services {
    position: absolute;
    left: 666px; top: 16px;
    list-style: none;
  }
  .services__item {
    display: flex; align-items: center;
    height: 30.5px;
    color: var(--white);
    font-weight: 700;
    font-size: 21px;
    letter-spacing: 0.01em;
  }
  .services__tick {
    width: 19px; height: 19px;
    margin-right: 10px;
    flex: none;
  }
  .sectors {
    position: absolute;
    left: 697px; top: 142px;
    display: grid;
    grid-template-columns: 127px 100px;
    row-gap: 2px;
    list-style: none;
  }
  .sectors__item {
    display: flex; align-items: center;
    color: var(--yellow);
    font-weight: 700;
    font-size: 14.5px;
    line-height: 18px;
    letter-spacing: 0.02em;
    white-space: nowrap;
  }
  .sectors__item::before {
    content: "";
    flex: none;
    width: 5px; height: 5px;
    background: var(--yellow);
    margin-right: 7px;
  }
</style>
</head>
<body>
  <section class="banner">
    <div class="banner__backdrop" role="img" aria-label="Dark monochrome photograph of steel scaffold tubes, couplers and checker-plate steel"></div>

    <svg class="banner__graphics" viewBox="0 0 1863 335" preserveAspectRatio="none" aria-hidden="true">
      <defs>
        <mask id="brand-clearance">
          <rect x="0" y="0" width="1863" height="335" fill="#fff"/>
          <rect x="78" y="228" width="490" height="56" fill="#000"/>
        </mask>
      </defs>
      <g mask="url(#brand-clearance)">
        <polygon points="0,0 0,20 290,309 330,309" fill="#000" opacity="0.35"/>
        <polyline points="0,20 280,309 0,309" fill="none" stroke="var(--yellow)" stroke-width="4"/>
        <polygon points="0,88 470,309 335,309 0,150" fill="var(--yellow)"/>
        <polygon points="0,72 470,309 470,319 0,84" fill="#cfcfcf" opacity="0.7"/>
      </g>
      <polygon points="700,0 795,0 525,187 455,187" fill="#0a0a0a" opacity="0.55"/>
      <line x1="795" y1="0" x2="525" y2="187" stroke="var(--yellow)" stroke-width="3"/>
      <line x1="1863" y1="75" x2="1470" y2="309" stroke="#8a8a8a" stroke-width="4"/>
      <polygon points="1863,115 1863,190 1710,292 1525,292" fill="var(--yellow)"/>
      <line x1="1700" y1="309" x2="1863" y2="309" stroke="var(--yellow)" stroke-width="4"/>
      <rect x="0" y="312" width="1863" height="23" fill="#2a2a2a"/>
      <rect x="470" y="312" width="1180" height="23" fill="var(--yellow)" opacity="0.85"/>
      <line x1="0" y1="309" x2="470" y2="309" stroke="var(--yellow)" stroke-width="4"/>
      <!-- brand mark placeholder: plain square -->
      <rect x="255" y="50" width="130" height="130" fill="#151515" stroke="var(--yellow)" stroke-width="7"/>
    </svg>

    <div class="brand-name">TRELBORN</div>

    <ul class="services">
      <li class="services__item">
        <svg class="services__tick" viewBox="0 0 20 20" aria-hidden="true"><rect x="1.5" y="3.5" width="15" height="15" fill="none" stroke="#f2b01e" stroke-width="2.2"/><polyline points="5,10 9,14 19,2" fill="none" stroke="#f2b01e" stroke-width="2.4"/></svg>
        SCAFFOLD DESIGN
      </li>
      <li class="services__item">
        <svg class="services__tick" viewBox="0 0 20 20" aria-hidden="true"><rect x="1.5" y="3.5" width="15" height="15" fill="none" stroke="#f2b01e" stroke-width="2.2"/><polyline points="5,10 9,14 19,2" fill="none" stroke="#f2b01e" stroke-width="2.4"/></svg>
        SCAFFOLD ENGINEERING
      </li>
      <li class="services__item">
        <svg class="services__tick" viewBox="0 0 20 20" aria-hidden="true"><rect x="1.5" y="3.5" width="15" height="15" fill="none" stroke="#f2b01e" stroke-width="2.2"/><polyline points="5,10 9,14 19,2" fill="none" stroke="#f2b01e" stroke-width="2.4"/></svg>
        SCAFFOLD INSTALLATION
      </li>
      <li class="services__item">
        <svg class="services__tick" viewBox="0 0 20 20" aria-hidden="true"><rect x="1.5" y="3.5" width="15" height="15" fill="none" stroke="#f2b01e" stroke-width="2.2"/><polyline points="5,10 9,14 19,2" fill="none" stroke="#f2b01e" stroke-width="2.4"/></svg>
        SCAFFOLD DISMANTLING
      </li>
    </ul>

    <ul class="sectors">
      <li class="sectors__item">COMMERCIAL</li>
      <li class="sectors__item">INDUSTRIAL</li>
      <li class="sectors__item">RESIDENTIAL</li>
      <li class="sectors__item">CIVIL</li>
    </ul>
  </section>
</body>
</html>
```